Advertisement Design Project

I would like to have some advertisement ideas to promote my business. Our company provides credit repair, tax preparation, notary service, ledger preparation (for small businesses and independent contractors) tax restoration (help people with liens, levy, garnishments, etc. by negotiating with the QVX in these matters)

The name of our company is Bel Arbor Financing
Our "CrestLumenPro" program focuses on tax preparation, restoration, and credit repair.
Our "Sunny Tracks" program prepares ledgers for small business and independent contractors by preparing monthly ledgers so that at tax season they are not having to look everywhere for their receipts in order to get all deductions due to them during the tax season.

We need something that is catchy and will gain attention

attached is our logo. Our slogan is "Happiness, Restored!"

Thank you!

Target Market(s)

The financially distressed
Small business owners
Independent contractors
businesses that rely on credit worthy clients to do business with

Industry/Entity Type

Small Business

Requirements
Must have
• great pictures
nice layout

```html
<!DOCTYPE html>
<html lang="en">
<head>
<meta charset="utf-8">
<title>Bel Arbor Financing – Flyer</title>
<link rel="stylesheet" href="https://fonts.googleapis.com/css2?family=PT+Sans:wght@400&display=swap">
<style>
  :root {
    --page-bg: #eef1f3;
    --ink-white: #ffffff;
    --title-blue: #8fd6f0;
    --brand-navy: #1d3f6e;
    --frame-white: #f4f4f4;
  }
  * { margin: 0; padding: 0; box-sizing: border-box; }
  html, body { width: 1200px; height: 864px; overflow: hidden; background: var(--page-bg); }
  body { font-family: "PT Sans", "Myriad Pro", Arial, sans-serif; }

  .flyer {
    position: absolute; left: 40px; top: 10px;
    width: 1120px; height: 844px; overflow: hidden;
    color: var(--ink-white);
  }
  .flyer__layer { position: absolute; inset: 0; width: 100%; height: 100%; }
  .flyer__layer--front { pointer-events: none; }

  .brand-title {
    position: absolute; left: 39px; top: 30px;
    font-size: 46px; font-weight: 400; color: var(--title-blue); letter-spacing: .2px;
  }
  .brand-slogan { position: absolute; left: 93px; top: 94px; font-size: 28px; }

  .brand-mark {
    position: absolute; left: 917px; top: 19px; width: 183px; height: 183px;
    border: 10px solid var(--frame-white); background: var(--brand-navy);
    display: flex; align-items: center; justify-content: center; text-align: center;
    box-shadow: 0 2px 6px rgba(0,0,0,.35);
  }
  .brand-mark__name { font-size: 22px; line-height: 1.25; color: var(--ink-white); padding: 0 12px; }

  .services { position: absolute; left: 33px; top: 218px; }
  .services__heading { font-size: 42px; font-weight: 400; margin-bottom: 4px; }
  .services__list { list-style: none; font-size: 26px; line-height: 35px; width: 385px; }

  .program { position: absolute; left: 426px; top: 256px; }
  .program__heading { font-size: 30px; font-weight: 400; margin-bottom: 2px; }
  .program__list { list-style: none; font-size: 26px; line-height: 35px; padding-left: 20px; }

  .photo {
    position: absolute; border: 6px solid var(--frame-white);
    box-shadow: 0 2px 8px rgba(0,0,0,.4);
  }
  .photo--desk { left: 158px; top: 637px; width: 334px; height: 157px;
    background: linear-gradient(100deg, #2f3338 0%, #6f7a84 30%, #d8dde2 55%, #f2f2f2 75%, #9aa3ab 100%); }
  .photo--meeting { left: 446px; top: 413px; width: 396px; height: 228px;
    background: linear-gradient(95deg, #f1f3f5 0%, #1f2d45 22%, #e6e2dc 45%, #f5f5f3 60%, #27354d 82%, #3a4656 100%); }
  .photo--tax { left: 803px; top: 276px; width: 300px; height: 196px;
    background: linear-gradient(140deg, #8c9a78 0%, #c9d1b6 30%, #efe6a8 55%, #a7adb1 78%, #5d6569 100%); }
  .photo--growth { left: 842px; top: 462px; width: 261px; height: 165px;
    background: radial-gradient(ellipse at 65% 45%, #7cc8e8 0%, #3f9fcc 35%, #dff1f9 70%, #ffffff 100%); }

  .contact-label { position: absolute; left: 830px; top: 678px; font-size: 26px; letter-spacing: .3px; }
</style>
</head>
<body>
<main class="flyer">
  <svg class="flyer__layer" viewBox="0 0 580 437" preserveAspectRatio="none" aria-hidden="true">
    <defs>
      <linearGradient id="field-gray" x1="0" y1="1" x2="1" y2="0">
        <stop offset="0" stop-color="#141414"/>
        <stop offset=".45" stop-color="#555"/>
        <stop offset="1" stop-color="#e4e4e4"/>
      </linearGradient>
      <linearGradient id="swoosh-blue" x1="0" y1="0" x2="1" y2="0">
        <stop offset="0" stop-color="#1c5fa8"/>
        <stop offset=".6" stop-color="#3aa3dc"/>
        <stop offset="1" stop-color="#bfe6f6"/>
      </linearGradient>
    </defs>
    <rect class="field" width="580" height="437" fill="url(#field-gray)"/>
    <path class="top-arc-light" d="M0,104 C70,116 210,112 380,0 H410 C240,110 90,128 0,116 Z" fill="#d0d0d0" opacity=".45"/>
    <path class="top-arc-blue" d="M40,110 C150,116 260,80 345,0 H372 C285,80 170,118 40,110 Z" fill="url(#swoosh-blue)"/>
    <path class="top-block" d="M0,0 H345 C300,45 250,88 170,102 C110,112 50,108 0,100 Z" fill="#0b0b0b"/>
  </svg>

  <h1 class="brand-title">Bel Arbor Financing</h1>
  <p class="brand-slogan">Happiness, Restored!</p>

  <div class="brand-mark"><span class="brand-mark__name">Bel Arbor Financing</span></div>

  <section class="services">
    <h2 class="services__heading">Company provides</h2>
    <ul class="services__list">
      <li>credit repair</li>
      <li>tax preparation</li>
      <li>notary service</li>
      <li>ledger preparation</li>
      <li>tax restoration (help people with liens, levy, garnishments, etc. by negotiating with the QVX in these matters)</li>
    </ul>
  </section>

  <section class="program">
    <h2 class="program__heading">"CrestLumenPro" program</h2>
    <ul class="program__list">
      <li>Tax preparation</li>
      <li>Restoration</li>
      <li>and credit repair.</li>
    </ul>
  </section>

  <div class="photo photo--desk" role="img" aria-label="Photo of a hand signing papers beside a laptop and phone on a desk"></div>
  <div class="photo photo--tax" role="img" aria-label="Photo of banknotes, a calculator and a note reading Tax Time on a spreadsheet"></div>
  <div class="photo photo--meeting" role="img" aria-label="Photo of a smiling couple shaking hands with an advisor at a desk"></div>
  <div class="photo photo--growth" role="img" aria-label="Illustration of a small blue figure pushing a large blue dollar sign"></div>

  <svg class="flyer__layer flyer__layer--front" viewBox="0 0 580 437" preserveAspectRatio="none" aria-hidden="true">
    <defs>
      <linearGradient id="swoosh-blue-b" x1="0" y1="0" x2="1" y2="0">
        <stop offset="0" stop-color="#1c5fa8"/>
        <stop offset=".6" stop-color="#3aa3dc"/>
        <stop offset="1" stop-color="#bfe6f6"/>
      </linearGradient>
      <linearGradient id="corner-gray" x1="0" y1="0" x2="1" y2="0">
        <stop offset="0" stop-color="#6d6d6d"/>
        <stop offset="1" stop-color="#d6d6d6"/>
      </linearGradient>
    </defs>
    <path class="bottom-block" d="M190,437 C250,370 380,330 580,330 V437 Z" fill="#0b0b0b"/>
    <path class="bottom-edge" d="M190,437 C250,370 380,330 580,330 V333 C382,334 256,372 196,437 Z" fill="#9a9a9a"/>
    <path class="bottom-arc-blue" d="M210,437 C270,405 340,390 440,388 C350,398 290,414 258,437 Z" fill="url(#swoosh-blue-b)"/>
    <path class="bottom-corner" d="M258,437 C310,410 420,396 580,396 V437 Z" fill="url(#corner-gray)"/>
  </svg>

  <p class="contact-label">CONTACT</p>
</main>
</body>
</html>
```